Boutique Barre Studio in Geneva

Business card for pilates and dance studio. We are a brand new studio and love our fresh image with our yellow color. This business card is meant for our founder.

```html
<!DOCTYPE html>
<html lang="en">
<head>
<meta charset="utf-8">
<title>Lumen Studio — Business Card</title>
<link rel="stylesheet" href="https://fonts.googleapis.com/css2?family=Arimo:wght@400;700&display=swap">
<style>
  :root {
    --backdrop: #1b1b1b;
    --card: #2a2a2a;
    --card-edge: #323232;
    --gold: #efe77a;
    --ink-light: #f2f2f2;
    --emboss: #3b3b3b;
  }
  * { margin: 0; padding: 0; box-sizing: border-box; }
  html, body {
    width: 1200px;
    height: 900px;
    overflow: hidden;
    background: var(--backdrop);
    font-family: "Arimo", Arial, sans-serif;
  }
  .canvas {
    position: relative;
    width: 1200px;
    height: 900px;
  }
  .card {
    position: absolute;
    left: 250px;
    width: 700px;
    height: 400px;
    background: linear-gradient(135deg, var(--card-edge), var(--card));
    border-radius: 18px;
    overflow: hidden;
  }
  .card--back { top: 30px; }
  .card--front { top: 470px; }

  .wordmark {
    position: absolute;
    font-weight: 700;
    letter-spacing: 0.04em;
    line-height: 1;
    white-space: nowrap;
  }
  .card--back .wordmark {
    left: 0; right: 0;
    top: 170px;
    text-align: center;
    font-size: 58px;
    color: var(--emboss);
  }
  .card--front .wordmark {
    right: 40px;
    top: 78px;
    font-size: 44px;
    color: var(--gold);
  }

  .holder {
    position: absolute;
    left: 44px;
    top: 40px;
  }
  .holder__name {
    font-size: 27px;
    font-weight: 700;
    letter-spacing: 0.03em;
    color: var(--gold);
  }
  .holder__title {
    margin-top: 4px;
    font-size: 16px;
    color: var(--ink-light);
  }

  .contacts {
    position: absolute;
    left: 44px;
    bottom: 40px;
    list-style: none;
  }
  .contacts__item {
    display: flex;
    align-items: center;
    gap: 12px;
    font-size: 18px;
    color: var(--ink-light);
    line-height: 1.75;
  }
  .contacts__icon {
    width: 18px;
    height: 18px;
    flex: none;
    fill: var(--gold);
  }

  .address {
    position: absolute;
    right: 40px;
    bottom: 40px;
    text-align: right;
    font-style: normal;
    font-size: 18px;
    line-height: 1.4;
    color: var(--ink-light);
  }
</style>
</head>
<body>
<main class="canvas">

  <section class="card card--back" aria-label="Card back">
    <p class="wordmark">LUMEN STUDIO</p>
  </section>

  <section class="card card--front" aria-label="Card front">
    <header class="holder">
      <h1 class="holder__name">CLARA VENNET</h1>
      <p class="holder__title">CEO/Founder</p>
    </header>

    <p class="wordmark">LUMEN STUDIO</p>

    <ul class="contacts">
      <li class="contacts__item">
        <svg class="contacts__icon" viewBox="0 0 24 24" aria-hidden="true">
          <path d="M6.6 10.8a15.1 15.1 0 0 0 6.6 6.6l2.2-2.2a1 1 0 0 1 1-.25 11.4 11.4 0 0 0 3.6.57 1 1 0 0 1 1 1V20a1 1 0 0 1-1 1A17 17 0 0 1 3 4a1 1 0 0 1 1-1h3.5a1 1 0 0 1 1 1c0 1.25.2 2.45.57 3.57a1 1 0 0 1-.25 1z"/>
        </svg>
        022-555-0148
      </li>
      <li class="contacts__item">
        <svg class="contacts__icon" viewBox="0 0 24 24" aria-hidden="true">
          <path d="M2 5h20v14H2z M3.5 6.5 12 13l8.5-6.5" fill="var(--gold)"/>
          <path d="M3.5 6.5 12 13l8.5-6.5" fill="none" stroke="var(--card)" stroke-width="1.6"/>
        </svg>
        hello@lumenstudio.ch
      </li>
      <li class="contacts__item">
        <svg class="contacts__icon" viewBox="0 0 24 24" aria-hidden="true">
          <circle cx="12" cy="12" r="10"/>
          <path d="M2 12h20M12 2c3 3 3 17 0 20M12 2c-3 3-3 17 0 20" fill="none" stroke="var(--card)" stroke-width="1.4"/>
        </svg>
        www.lumenstudio.ch
      </li>
    </ul>

    <address class="address">
      14 Rue des Lilas<br>
      Geneva, GE 1204
    </address>
  </section>

</main>
</body>
</html>
```